Bloom and Rise Website Design (design layout only)

We need a website design for a new nonprofit organization based in Des Moines, Iowa called Bloom and Rise. The nonprofit provides soccer training opportunities to youth soccer players looking to improve their game while also affecting the lives of the less fortunate in a positive way. While participating in the training programs the players also go out and raise money for selected charities. The organization then donates the funds. In its first 18 months we donated $10,500. We would like to see designs attempt to symbolize the mission of the nonprofit - essentially "improve you while improving someone else."

We would like to see the following features:

· A place to donate - Our intent is to have the home page linked to the donation page; a simple straight-forward process for people to give money, and make donating as painless as possible - no account needed to make a donation, credit card or e-check should be the only information needed to donate, and have it be on a single page.

· A photo gallery so people can browse the photo gallery to get a better understanding of our organization and a place to add videos and a calendar to show upcoming events

· A place for contact information and the profiles of directors and board members. This should include a spot showing all the charities the organization donates to. Also includes a news section/blog for comments and suggestions.

We want the design to revolve around the content and mission. We would really like to stress our organization as nonprofit. We would also like if the website was user friendly and easy to navigate.

The logo of our organization is uploaded

```html
<!DOCTYPE html>
<html lang="en">
<head>
<meta charset="utf-8">
<title>Bloom and Rise</title>
<link href="https://fonts.googleapis.com/css2?family=Oswald:wght@300;400;500;600&family=Open+Sans:wght@400;600&display=swap" rel="stylesheet">
<style>
:root{
  --green:#6f9a4b;
  --green-dark:#4f7a32;
  --green-light:#9dbb7d;
  --blue:#1d4fa3;
  --blue-dark:#163f86;
  --ink:#333;
  --muted:#777;
  --footer:#a3a3a3;
  --black:#0b0b0b;
  --white:#fff;
}
*{margin:0;padding:0;box-sizing:border-box}
html,body{width:752px;height:1200px;overflow:hidden;background:var(--white)}
body{font-family:"Open Sans",sans-serif;color:var(--ink)}
.page{position:relative;width:752px;height:1200px;overflow:hidden}
.abs{position:absolute}
.hero{left:0;top:0;width:752px;height:344px;
  background:
    radial-gradient(ellipse 260px 120px at 480px 250px,rgba(90,150,60,.55),transparent 70%),
    linear-gradient(180deg,#070807 0%,#111511 30%,#1e2a1b 48%,#3d6b2b 66%,#4f8236 82%,#3f6e2b 100%)}
.topbar{left:0;top:0;width:752px;height:37px;background:#efefef}
.brand{left:96px;top:0;width:181px;height:76px;background:#f2f2f2;border:1px solid #d6d6d6;display:flex;align-items:center;justify-content:center;gap:7px}
.brand .dot{width:14px;height:14px;border-radius:50%;background:var(--green)}
.brand span{font-family:"Oswald",sans-serif;font-weight:600;font-size:21px;color:var(--green);letter-spacing:.5px}
.nav{left:292px;top:0;height:37px;display:flex;align-items:center}
.nav a{font-family:"Oswald",sans-serif;font-size:8.5px;color:#3f5a2a;text-decoration:none;padding:0 5px;height:37px;line-height:37px}
.nav a.active{background:#dedede}
.nav-donate{left:615px;top:0;width:66px;height:37px;background:var(--green);color:var(--white);font-family:"Oswald",sans-serif;font-size:9px;display:flex;align-items:center;justify-content:center;gap:5px}
.nav-donate i{width:10px;height:10px;border-radius:50%;background:var(--white);display:block}
.headline{left:86px;top:96px;width:400px;text-align:right;font-family:"Oswald",sans-serif;color:var(--white);text-transform:uppercase;white-space:nowrap}
.headline .l1{font-size:36px;font-weight:500;line-height:44px;letter-spacing:-1.2px}
.headline .l1 em{font-style:normal;font-weight:300}
.headline .l2{font-size:26px;font-weight:500;line-height:30px;letter-spacing:-.8px}
.donatebar{left:106px;top:273px;width:575px;height:70px;background:var(--blue);display:flex;color:var(--white);font-family:"Oswald",sans-serif}
.donatebar .stat{width:106px;background:var(--blue-dark);text-align:center;padding-top:14px}
.stat .k{font-weight:300;font-size:13px;display:block}
.stat .v{font-weight:500;font-size:19px;display:block;line-height:22px}
.donatebar .mid{flex:1;display:flex;align-items:center;padding-left:28px}
.mid .give{font-weight:300;font-size:11px;line-height:12px}
.mid .give strong{display:block;font-weight:500;font-size:19px;line-height:24px}
.mid p{font-family:"Open Sans",sans-serif;font-size:6.5px;line-height:9px;width:130px;margin-left:8px}
.mid .btn{margin-left:22px;background:var(--white);color:var(--blue);font-weight:500;font-size:11px;width:99px;height:21px;line-height:21px;text-align:center}
.stripe{height:9px;background:repeating-linear-gradient(135deg,var(--green-light) 0 3px,#c6dab1 3px 6px)}
.gallery-panel{left:106px;top:352px;width:575px;height:154px;background:var(--white);box-shadow:0 3px 8px rgba(0,0,0,.12)}
.title{font-family:"Oswald",sans-serif;font-weight:300;font-size:14px;color:var(--green);display:flex;align-items:center;gap:5px;padding-bottom:3px;border-bottom:2px solid var(--green-light)}
.title i{width:13px;height:13px;border-radius:50%;border:2px solid var(--green-dark);display:block;background:var(--white)}
.thumb{width:127px;height:70px;border:3px solid #eee;box-shadow:0 1px 3px rgba(0,0,0,.3)}
.caption{width:127px;font-size:5.5px;line-height:8.5px;text-align:center;color:var(--muted)}
.member{width:110px;text-align:center}
.member .photo{width:72px;height:72px;border-radius:50%;margin:0 auto;background:radial-gradient(circle at 50% 40%,#4a6a8a,#1f3550 70%)}
.member h3{font-family:"Oswald",sans-serif;font-weight:400;font-size:11px;color:#333;margin-top:7px}
.member p{font-size:6.5px;color:#555;margin-top:2px}
.news-item{left:126px;width:320px;display:flex;gap:8px}
.date{width:34px;height:34px;border-radius:50%;background:var(--green-dark);color:var(--white);font-family:"Oswald",sans-serif;text-align:center;flex:none;padding-top:4px}
.date b{display:block;font-weight:400;font-size:12px;line-height:13px}
.date small{font-size:7px;display:block}
.news-item h4{font-weight:400;font-size:8px;color:var(--green)}
.news-item p{font-size:5.5px;line-height:8px;color:var(--muted)}
.events{left:477px;top:794px;width:204px;height:171px;border:1px solid #d3d3d3;border-radius:3px;background:linear-gradient(#fff,#eaeaea);padding:8px 16px}
.events h3{font-family:"Oswald",sans-serif;font-weight:500;font-size:17px;color:var(--green);text-align:center;margin-bottom:6px}
.event{display:flex;justify-content:space-between;align-items:flex-end;border-bottom:1px solid #cfd9c4;padding:8px 0 4px;font-family:"Oswald",sans-serif;font-weight:300}
.event span{font-size:10px;color:var(--green)}
.event small{font-size:7px;color:#444}
.partners{left:106px;top:993px;width:575px;height:58px;background:var(--black);display:flex;align-items:center;padding-left:15px}
.partners h2{font-family:"Oswald",sans-serif;font-weight:300;font-size:15px;color:var(--green-light)}
.partners .brace{width:6px;height:38px;border:2px solid var(--green);border-left:none;border-radius:0 8px 8px 0;margin:0 30px 0 8px}
.badge{width:60px;height:16px;background:#555;border-radius:3px;margin-right:24px}
.foot-stripe{left:0;top:1070px;width:752px;height:6px;background:repeating-linear-gradient(135deg,var(--green-light) 0 2px,transparent 2px 4px)}
.footer{left:0;top:1078px;width:752px;height:122px;background:var(--footer);color:var(--white)}
.fcol h4{font-weight:400;font-size:9.5px;margin-bottom:4px}
.fcol a{display:block;color:var(--white);text-decoration:none;font-size:7px;line-height:16px}
.fbrand{left:512px;top:22px;display:flex;align-items:center;gap:7px}
.fbrand .dot{width:16px;height:16px;border-radius:50%;background:var(--white)}
.fbrand span{font-family:"Oswald",sans-serif;font-weight:600;font-size:24px;color:var(--white)}
.social{left:580px;top:74px;display:flex;gap:9px}
.social i{width:17px;height:17px;border-radius:50%;background:#c3c3c3;display:block}
.copy{left:569px;top:102px;font-size:7.5px}
</style>
</head>
<body>
<div class="page">
  <div class="abs hero" role="img" aria-label="Photo of a player's legs with a soccer ball and orange training cones on a floodlit pitch"></div>
  <div class="abs topbar"></div>
  <nav class="abs nav">
    <a class="active" href="#">HOME</a><a href="#">ABOUT US</a><a href="#">NEWS</a><a href="#">TRAINING PROGRAMS</a><a href="#">UPCOMING EVENTS</a><a href="#">GALLERY</a><a href="#">CONTACT</a>
  </nav>
  <div class="abs nav-donate"><i></i>DONATE</div>
  <div class="abs brand"><div class="dot"></div><span>BLOOM AND RISE</span></div>

  <h1 class="abs headline">
    <div class="l1">Improve Yourself <em>While</em></div>
    <div class="l2">Improving Someone Else</div>
  </h1>

  <div class="abs donatebar">
    <div class="stat"><span class="k">Our Goal</span><span class="v">$20,000</span></div>
    <div class="mid">
      <div class="give">Give Us<strong>DONATION</strong></div>
      <p>Lorem ipsum dolor sit amet, consetuer adipiscing elit, sed diammy dolore magna aliquam erat volutpat.</p>
      <div class="btn">DONATE NOW!</div>
    </div>
    <div class="stat"><span class="k">More Needed</span><span class="v">$10,000</span></div>
  </div>
  <div class="abs stripe" style="left:106px;top:343px;width:575px"></div>

  <section class="abs gallery-panel"></section>
  <h2 class="abs title" style="left:124px;top:365px;width:104px"><i></i>GALLERY</h2>
  <div class="abs thumb" style="left:125px;top:397px;background:linear-gradient(#0e1a33,#1c3260)" role="img" aria-label="Night training session on a dark pitch"></div>
  <div class="abs thumb" style="left:261px;top:397px;background:linear-gradient(#3a2a28,#8a3b33)" role="img" aria-label="Players challenging for a header in front of a crowd"></div>
  <div class="abs thumb" style="left:397px;top:397px;background:linear-gradient(#3f6a2c,#7a5a2e)" role="img" aria-label="Team huddle on a green field"></div>
  <div class="abs thumb" style="left:533px;top:397px;background:linear-gradient(#6f8a6a,#4d8a35)" role="img" aria-label="Youth players training on grass near a goal"></div>
  <p class="abs caption" style="left:115px;top:480px">Lorem ipsum dolor sit amet, consectetuer adipiscing elit, sed diam nonummy dolore magna aliquam erat volutpat.</p>
  <p class="abs caption" style="left:252px;top:480px">Lorem ipsum dolor sit amet, consectetuer adipiscing elit, sed diam nonummy dolore magna aliquam erat volutpat.</p>
  <p class="abs caption" style="left:391px;top:480px">Lorem ipsum dolor sit amet, consectetuer adipiscing elit, sed diam nonummy dolore magna aliquam erat volutpat.</p>
  <p class="abs caption" style="left:535px;top:480px">Lorem ipsum dolor sit amet, consectetuer adipiscing elit, sed diam nonummy dolore magna aliquam erat volutpat.</p>

  <h2 class="abs title" style="left:124px;top:562px;width:104px"><i></i>OUR TEAM</h2>
  <div class="abs member" style="left:129px;top:597px"><div class="photo" role="img" aria-label="Portrait of Dale Brennan"></div><h3>Dale Brennan</h3><p>CEO</p></div>
  <div class="abs member" style="left:226px;top:597px"><div class="photo" role="img" aria-label="Portrait of Sharon Jessup"></div><h3>Sharon Jessup</h3><p>Manager</p></div>
  <div class="abs member" style="left:319px;top:597px"><div class="photo" role="img" aria-label="Portrait of Miles Blane"></div><h3>Miles Blane</h3><p>Accountant</p></div>
  <div class="abs member" style="left:411px;top:597px"><div class="photo" role="img" aria-label="Portrait of Marcus Anton"></div><h3>Marcus Anton</h3><p>Team Leader</p></div>
  <div class="abs member" style="left:510px;top:597px"><div class="photo" role="img" aria-label="Portrait of Joan Sholes"></div><h3>Joan Sholes</h3><p>Audit &amp; Accounts Team</p></div>

  <h2 class="abs title" style="left:129px;top:761px;width:104px"><i></i>NEWS</h2>
  <h2 class="abs title" style="left:477px;top:761px;width:146px"><i></i>UPCOMING EVENTS</h2>

  <article class="abs news-item" style="top:800px"><div class="date"><b>23</b><small>JUL</small></div><div><h4>searchable version</h4><p>Spring clinic players raised funds for a local food pantry through weekend skill sessions and sponsor walks.</p></div></article>
  <article class="abs news-item" style="top:864px"><div class="date"><b>23</b><small>JUL</small></div><div><h4>searchable version</h4><p>Spring clinic players raised funds for a local food pantry through weekend skill sessions and sponsor walks.</p></div></article>
  <article class="abs news-item" style="top:926px"><div class="date"><b>23</b><small>JUL</small></div><div><h4>searchable version</h4><p>Spring clinic players raised funds for a local food pantry through weekend skill sessions and sponsor walks.</p></div></article>

  <aside class="abs events">
    <h3>PROPOSED DATES</h3>
    <div class="event"><span>Trivia Night</span><small>9th August</small></div>
    <div class="event"><span>Junior Presentation day &amp; AGM</span><small>7th June</small></div>
    <div class="event"><span>Senior Presentation day</span><small>11th October</small></div>
    <div class="event"><span>Junior Presentation day &amp; AGM</span><small>7th June</small></div>
  </aside>

  <section class="abs partners">
    <h2>OUR PARTNERS</h2><div class="brace"></div>
    <div class="badge"></div><div class="badge"></div><div class="badge"></div><div class="badge"></div><div class="badge"></div>
  </section>

  <div class="abs foot-stripe"></div>
  <footer class="abs footer">
    <div class="abs fcol" style="left:106px;top:14px"><h4>Infomation</h4><a href="#">Home</a><a href="#">About club</a><a href="#">Our team</a><a href="#">Contacts</a><a href="#">Blog</a></div>
    <div class="abs fcol" style="left:342px;top:13px"><h4>Support</h4><a href="#">Terms of Service</a><a href="#">Security</a><a href="#">Privacy Policy</a><a href="#">Sitemap</a><a href="#">FAQ</a></div>
    <div class="abs fbrand"><div class="dot"></div><span>BLOOM AND RISE</span></div>
    <div class="abs social"><i></i><i></i><i></i><i></i></div>
    <p class="abs copy">© 2014 - All Rights Reserved</p>
  </footer>
</div>
</body>
</html>
```